Brightpath Property College Needs Banner Designs

I just launched an online real estate school at www.brightpathpropertycollege.com

I am seeking designers to work on 2 banners (listed seperately) as well as a a Facebook design. This listing is for 1 of 2 banners.

First banner I intend to use on different job offering web sites. So "Launch your career into Real Estate" could be the concept. i'm open to 1 sentence pitch's. please look at my website to view graphics and colors.

```html
<!DOCTYPE html>
<html lang="en">
<head>
<meta charset="utf-8">
<title>Brightpath Property College – Banner Set</title>
<link rel="stylesheet" href="https://fonts.googleapis.com/css2?family=Nunito+Sans:wght@400;600;700;800;900&display=swap">
<style>
  :root {
    --navy: #0b3a73;
    --navy-deep: #1c3566;
    --orange: #f7941d;
    --gold-top: #ffd21f;
    --gold-bottom: #f2a700;
    --ink: #222222;
    --btn-ink: #3a2a00;
    --photo-light: #ece2bb;
    --photo-mid: #c9b98a;
    --photo-dark: #7d735a;
    --note-red: #e0201b;
    --page: #f1f1ef;
  }
  * { box-sizing: border-box; margin: 0; padding: 0; }
  html, body { width: 1200px; height: 910px; overflow: hidden; }
  body {
    background: var(--page);
    font-family: "Nunito Sans", Arial, sans-serif;
    position: relative;
  }
  .sheet-label {
    position: absolute; left: 50px; top: 18px;
    font-family: Arial, Helvetica, sans-serif;
    font-size: 19px; color: #333;
  }
  .cover { position: absolute; left: 38px; top: 54px; width: 1073px; height: 408px; }
  .cover text { font-family: "Nunito Sans", Arial, sans-serif; }

  .banner { position: absolute; overflow: hidden; background: var(--photo-mid); }
  .photo {
    position: absolute; inset: 0;
    background:
      radial-gradient(ellipse at 70% 30%, rgba(255,250,220,0.9), rgba(255,250,220,0) 60%),
      linear-gradient(180deg, var(--photo-light) 0%, var(--photo-mid) 55%, var(--photo-dark) 100%);
  }
  .headline {
    position: absolute; background: var(--navy); color: #fff;
    text-align: center; font-weight: 800; line-height: 1.05;
    display: flex; flex-direction: column; justify-content: center; align-items: center;
  }
  .headline .career { color: var(--orange); font-weight: 900; line-height: 1; }
  .brand-name {
    position: absolute; color: var(--navy); font-weight: 800;
    text-align: center; line-height: 1.1;
  }
  .details { position: absolute; color: var(--ink); font-weight: 700; text-align: center; }
  .pitch { position: absolute; color: var(--ink); font-weight: 800; text-align: center; line-height: 1.15; }
  .visit-btn {
    position: absolute; border-radius: 999px;
    background: linear-gradient(180deg, var(--gold-top), var(--gold-bottom));
    color: var(--btn-ink); font-weight: 800;
    display: flex; align-items: center; justify-content: center;
    box-shadow: 0 1px 2px rgba(0,0,0,0.25);
  }

  /* square 165 */
  .banner--square { left: 38px; top: 533px; width: 165px; height: 165px; }
  .banner--square .headline { left: 52px; top: 2px; width: 103px; height: 70px; font-size: 8px; }
  .banner--square .headline .career { font-size: 22px; }
  .banner--square .brand-name { left: 40px; top: 100px; width: 125px; font-size: 10px; }
  .banner--square .visit-btn { left: 56px; top: 138px; width: 92px; height: 18px; font-size: 11px; }

  /* medium rectangle */
  .banner--rect { left: 260px; top: 503px; width: 547px; height: 207px; }
  .banner--rect .headline { left: 25px; top: 1px; width: 144px; height: 102px; font-size: 13px; }
  .banner--rect .headline .career { font-size: 32px; }
  .banner--rect .brand-name { left: 320px; top: 70px; width: 160px; font-size: 19px; }
  .banner--rect .details { left: 322px; top: 140px; width: 150px; font-size: 10px; }
  .banner--rect .visit-btn { left: 322px; top: 158px; width: 150px; height: 33px; font-size: 18px; }

  /* leaderboard */
  .banner--leader { left: 325px; top: 732px; width: 482px; height: 60px; }
  .banner--leader .headline { left: 0; top: 0; width: 130px; height: 60px; font-size: 8px; }
  .banner--leader .headline .career { font-size: 24px; }
  .banner--leader .headline .sub { font-size: 10px; }
  .banner--leader .pitch { left: 160px; top: 22px; width: 125px; font-size: 8px; text-align: left; }
  .banner--leader .brand-name { left: 288px; top: 17px; width: 62px; font-size: 7px; }
  .banner--leader .details { left: 376px; top: 16px; width: 91px; font-size: 7px; }
  .banner--leader .visit-btn { left: 376px; top: 28px; width: 91px; height: 18px; font-size: 10px; }

  /* half page */
  .banner--tall { left: 832px; top: 478px; width: 199px; height: 396px; }
  .banner--tall .headline { left: 0; top: 0; width: 199px; height: 101px; font-size: 12px; }
  .banner--tall .headline .career { font-size: 31px; }
  .banner--tall .headline .sub { font-size: 19px; }
  .banner--tall .pitch { left: 56px; top: 181px; width: 140px; font-size: 16px; }
  .banner--tall .brand-name { left: 60px; top: 268px; width: 130px; font-size: 13px; }
  .banner--tall .details { left: 42px; top: 326px; width: 148px; font-size: 9px; }
  .banner--tall .visit-btn { left: 42px; top: 343px; width: 148px; height: 33px; font-size: 18px; }

  /* skyscraper */
  .banner--sky { left: 1058px; top: 478px; width: 106px; height: 396px; }
  .banner --sky {}
  .banner--sky .headline { left: 0; top: 0; width: 106px; height: 110px; font-size: 7px; }
  .banner--sky .headline .career { font-size: 20px; }
  .banner--sky .headline .sub { font-size: 11px; }
  .banner--sky .brand-name { left: 36px; top: 292px; width: 70px; font-size: 8px; }
  .banner--sky .visit-btn { left: 20px; top: 352px; width: 79px; height: 16px; font-size: 9px; }

  .size-note {
    position: absolute; left: 41px; top: 848px;
    font-family: Arial, Helvetica, sans-serif; font-size: 18px;
    color: var(--note-red); text-decoration: underline;
  }
</style>
</head>
<body>
  <div class="sheet-label">FACEBOOK</div>

  <svg class="cover" viewBox="0 0 1316 500" xmlns="http://www.w3.org/2000/svg">
    <rect width="1316" height="500" fill="#ffffff"/>
    <polygon points="0,25 356,290 517,147 797,380 960,282 1140,410 1140,500 0,500" fill="var(--navy)"/>
    <polygon points="0,25 98,96 98,500 0,500" fill="var(--navy-deep)"/>

    <polyline points="150,125 356,240 517,97 797,332 960,242 1140,356"
      fill="none" stroke="#ffffff" stroke-width="36" stroke-linejoin="miter"/>
    <polyline points="150,125 356,240 517,97 797,332 960,242 1140,356"
      fill="none" stroke="var(--orange)" stroke-width="22" stroke-linejoin="miter"/>

    <g role="img" aria-label="Orange rocket illustration launching the career path">
      <rect x="-10" y="40" width="180" height="50" rx="25" fill="var(--orange)" transform="rotate(30 80 65)"/>
    </g>

    <g class="path-stops" fill="none" stroke="#ffffff" stroke-width="2">
      <line x1="182" y1="143" x2="182" y2="320"/>
      <line x1="356" y1="240" x2="356" y2="392"/>
      <line x1="517" y1="97" x2="517" y2="275"/>
      <line x1="797" y1="332" x2="797" y2="420"/>
      <line x1="960" y1="242" x2="960" y2="339"/>
    </g>
    <g fill="#ffffff">
      <circle cx="182" cy="320" r="6"/><circle cx="356" cy="392" r="6"/>
      <circle cx="517" cy="275" r="6"/><circle cx="797" cy="420" r="6"/>
      <circle cx="960" cy="339" r="6"/>
    </g>
    <g>
      <circle cx="182" cy="143" r="20" fill="#fff" stroke="var(--orange)" stroke-width="6"/><circle cx="182" cy="143" r="6" fill="var(--orange)"/>
      <circle cx="356" cy="240" r="20" fill="#fff" stroke="var(--orange)" stroke-width="6"/><circle cx="356" cy="240" r="6" fill="var(--orange)"/>
      <circle cx="517" cy="97" r="20" fill="#fff" stroke="var(--orange)" stroke-width="6"/><circle cx="517" cy="97" r="6" fill="var(--orange)"/>
      <circle cx="797" cy="332" r="20" fill="#fff" stroke="var(--orange)" stroke-width="6"/><circle cx="797" cy="332" r="6" fill="var(--orange)"/>
      <circle cx="960" cy="242" r="20" fill="#fff" stroke="var(--orange)" stroke-width="6"/><circle cx="960" cy="242" r="6" fill="var(--orange)"/>
    </g>

    <g class="stop-labels" fill="#ffffff" font-size="16" font-weight="700">
      <text x="196" y="308">Train on</text>
      <text x="196" y="328">Your Schedule</text>
      <text x="361" y="428" text-anchor="middle">Meets State License</text>
      <text x="361" y="448" text-anchor="middle">Requirements</text>
      <text x="517" y="317" text-anchor="middle">State-Approved Courses</text>
      <text x="806" y="452" text-anchor="middle">Convenient 100%</text>
      <text x="806" y="472" text-anchor="middle">Online Courses</text>
      <text x="956" y="384" text-anchor="middle">Quick, Easy, and</text>
      <text x="956" y="404" text-anchor="middle">Affordable</text>
    </g>

    <text x="641" y="112" font-size="34" font-weight="800" fill="var(--ink)">LAUNCH YOUR</text>
    <text x="1245" y="125" font-size="88" font-weight="900" fill="var(--orange)" text-anchor="end">CAREER</text>
    <text x="1245" y="170" font-size="32" font-weight="800" fill="var(--ink)" text-anchor="end">INTO REAL ESTATE</text>

    <g role="img" aria-label="Cartoon student working at a laptop on a desk">
      <rect x="1100" y="255" width="210" height="245" rx="20" fill="#d9c7a8"/>
    </g>

    <rect x="86" y="365" width="155" height="135" fill="#ffffff"/>
    <text x="163" y="430" font-size="17" font-weight="800" fill="var(--navy)" text-anchor="middle">Brightpath</text>
    <text x="163" y="452" font-size="17" font-weight="800" fill="var(--navy)" text-anchor="middle">Property College</text>
  </svg>

  <div class="banner banner--square">
    <div class="photo" role="img" aria-label="Businessman with briefcase walking down a sunlit road with the word career painted on it"></div>
    <div class="headline"><span>LAUNCH YOUR</span><span class="career">CAREER</span><span>INTO</span><span>REAL ESTATE</span></div>
    <div class="brand-name">Brightpath<br>Property College</div>
    <div class="visit-btn">Visit Now</div>
  </div>

  <div class="banner banner--rect">
    <div class="photo" role="img" aria-label="Businessman with briefcase walking down a sunlit road toward a city with the word career painted on it"></div>
    <div class="headline"><span>LAUNCH YOUR</span><span class="career">CAREER</span><span>INTO</span><span>REAL ESTATE</span></div>
    <div class="brand-name">Brightpath<br>Property College</div>
    <div class="details">For More Details</div>
    <div class="visit-btn">Visit Now</div>
  </div>

  <div class="banner banner--leader">
    <div class="photo" role="img" aria-label="Sunlit road leading toward a city skyline"></div>
    <div class="headline"><span>LAUNCH YOUR</span><span class="career">CAREER</span><span class="sub">INTO REAL ESTATE</span></div>
    <div class="pitch">Quick, Easy, and Affordable</div>
    <div class="brand-name">Brightpath<br>Property College</div>
    <div class="details">For More Details</div>
    <div class="visit-btn">Visit Now</div>
  </div>

  <div class="banner banner--tall">
    <div class="photo" role="img" aria-label="Businessman with briefcase walking down a sunlit road with the word career painted on it"></div>
    <div class="headline"><span>LAUNCH YOUR</span><span class="career">CAREER</span><span class="sub">INTO REAL ESTATE</span></div>
    <div class="pitch">Quick, Easy, and Affordable</div>
    <div class="brand-name">Brightpath<br>Property College</div>
    <div class="details">For More Details</div>
    <div class="visit-btn">Visit Now</div>
  </div>

  <div class="banner banner--sky">
    <div class="photo" role="img" aria-label="Businessman walking down a sunlit road with the word career painted on it"></div>
    <div class="headline"><span>LAUNCH YOUR</span><span class="career">CAREER</span><span class="sub">INTO</span><span class="sub">REAL ESTATE</span></div>
    <div class="brand-name">Brightpath<br>Property College</div>
    <div class="visit-btn">Visit Now</div>
  </div>

  <p class="size-note">* Most Recommended Sizes For Different Web And Can Be Change In To Other Required Sizes.</p>
</body>
</html>
```